New look for an established Travel booking site
10 year old design needs a new clean look and better usability
New look for an established Travel booking site - Travel
Creative Brief
Travel
lodgingmeadow.co.uk
We are a uk based web development company with over 10 years of experience. We often use external designers and have run several competitions on another design site, choosing a winner on each occasion.
Like: simple search box high on left hand side, eg http://www.nightquill.com/ navigation layout on http://www.roamfable.com/ (as in 'plan the perfect trip') blue colours in header of http://www.quietbarrow.co.uk/ clear layout in http://herefordshire.bedpeak.co.uk/ Dislikes: clutter too flashy
Service Oriented
#006633 or similar #4D7F3B etc for page background maybe
left side
http://www.roamfable.com/
http://herefordshire.bedpeak.co.uk/
http://nightquill.com
We are certainly NOT looking for a cut and paste job on the above websites! They are listed to give you an idea of the features we want to see on the page, we need to finish up with a page that is clean, attractive, and not confusing to the visitor. There need to be room for the current ads, and the home page will carry a uk map, but about 30% of the size of the current one. Green and blue for basic page colours.. There will be a photo on the homepage... probably an example of a hotel on site - eg http://www.lodgingmeadow.co.uk/places/307.html Existing site: lodgingmeadow.co.uk

```html
<!DOCTYPE html>
<html lang="en">
<head>
<meta charset="utf-8">
<title>Lodging Meadow</title>
<link href="https://fonts.googleapis.com/css2?family=Cinzel:wght@700&family=Lora:wght@400;700&family=Arimo:wght@400;700&display=swap" rel="stylesheet">
<style>
:root{
  --bg-top:#a7c49a;
  --bg:#7da36e;
  --bg-dark:#5f8a52;
  --blue:#7c83d0;
  --blue-light:#b7bbe8;
  --blue-dark:#4b51a3;
  --side:#9fbd90;
  --side-dark:#7fa170;
  --card:#a9c59b;
  --white:#ffffff;
  --text:#444;
  --olive:#8a9a3c;
  --head:#5f6aa8;
}
*{box-sizing:border-box;margin:0;padding:0}
html,body{width:1200px;height:961px;overflow:hidden}
body{
  background:linear-gradient(var(--bg-top) 0,var(--bg) 60px,var(--bg) 100%);
  font-family:'Arimo',Arial,sans-serif;color:var(--text);font-size:9px;position:relative;
}
.page{position:absolute;left:305px;top:12px;width:594px;height:886px;background:var(--white);border-radius:22px;overflow:hidden;border:3px solid var(--blue-light)}
.header{height:102px;background:linear-gradient(180deg,var(--blue-light),var(--blue) 55%,var(--blue-dark));position:relative}
.header .map{position:absolute;left:20px;top:8px;width:76px;height:88px;border-radius:8px;background:linear-gradient(135deg,#e8eaf8,#c3c7ee)}
.header .brand{position:absolute;left:170px;top:26px;font-family:'Cinzel',serif;font-size:24px;color:var(--white);letter-spacing:1px}
.header .tagline{position:absolute;left:215px;top:58px;font-family:'Cinzel',serif;font-size:11px;color:var(--white);letter-spacing:1px}
.nav{height:14px;background:var(--bg-dark);display:flex;gap:14px;padding-left:8px;align-items:center}
.nav a{color:var(--white);font-size:7px;font-weight:700;text-decoration:none;letter-spacing:.5px}
.strip{display:flex;height:114px;margin-top:4px}
.strip div{flex:1}
.p1{background:linear-gradient(#8fb1d9,#b7a88a 60%,#6b7d55)}
.p2{background:linear-gradient(#6fa0d8,#8a7048 55%,#5a4a32)}
.p3{background:linear-gradient(#2b2218,#d8a04a 50%,#3a2e22)}
.p4{background:linear-gradient(#7aa6dc,#4e6a8c 55%,#2e3d52)}
.body{display:flex;height:604px}
.side{width:140px;background:linear-gradient(var(--side),var(--side-dark));padding:10px 8px;color:var(--white);font-size:7px}
.side h4{font-size:7px;font-weight:700;margin:10px 0 4px;letter-spacing:.3px}
.side .rule{height:1px;background:rgba(255,255,255,.6);margin:4px 0}
.side input{width:100%;height:11px;border:1px solid #888;background:var(--white);display:block;margin:3px 0}
.btn{display:inline-block;background:var(--blue);color:var(--white);font-size:7px;padding:2px 8px;border:1px solid var(--blue-dark);margin-top:3px}
.hotels{margin:12px 6px;background:var(--blue);border:1px solid var(--blue-dark);padding:6px;height:178px}
.hotels h5{font-size:9px;color:var(--white);margin-bottom:8px}
.sel{height:11px;background:var(--white);border:1px solid #888;margin:6px 0;font-size:6px;color:#333;padding-left:2px;line-height:9px}
.side ul{list-style:square;padding-left:10px;line-height:10px}
.side .ads{color:var(--olive);font-family:'Lora',serif;font-size:10px;margin-top:10px}
.main{flex:1;padding:8px 8px}
.sec{font-family:'Lora',serif;font-size:14px;color:var(--head);letter-spacing:1px}
.bar{height:9px;background:var(--blue-light);margin:3px 0 6px;font-size:6px;color:#666;padding-left:3px;line-height:9px}
.title{font-family:'Lora',serif;font-size:12px;color:var(--head);margin-top:4px}
.meta{font-size:6px;color:#777;margin:4px 0}
.more{font-size:6px;color:var(--blue-dark);text-decoration:underline}
.welcome{display:flex;gap:12px;margin-top:6px}
.welcome h3{font-family:'Lora',serif;font-size:13px;color:var(--head);margin-bottom:6px}
.welcome p{font-size:6.5px;line-height:9px;color:#666;width:290px}
.hotelphoto{width:118px;height:148px;background:linear-gradient(#3c5890,#c7a46a 55%,#4a3a28);flex:none}
.cards{display:flex;gap:10px;margin-top:22px}
.card{flex:1;background:var(--card);height:248px;padding:10px;border:1px solid var(--side-dark)}
.card .row{display:flex;gap:6px}
.card .img{width:100px;height:118px;flex:none}
.c1{background:linear-gradient(#8fb4e0,#c2b08c 60%,#6e8a5a)}
.c2{background:linear-gradient(#7ba7df,#a87c40 60%,#4f6078)}
.card .side-t{font-family:'Lora',serif;font-size:10px;color:var(--white);line-height:13px}
.card h6{font-family:'Lora',serif;font-size:10px;color:var(--white);font-weight:400;line-height:13px;margin-top:10px}
.card p{font-size:6px;color:#555;line-height:8px;margin-top:6px}
.footer{height:34px;background:linear-gradient(var(--blue),var(--blue-dark));color:var(--white);font-size:6px;text-align:center;padding-top:8px;position:relative;line-height:8px}
.footer .dot{position:absolute;left:8px;top:12px;width:9px;height:9px;border-radius:50%;background:#e8a040}
.powered{position:absolute;top:910px;left:0;width:1200px;text-align:center;color:var(--white);font-size:6px}
</style>
</head>
<body>
<div class="page">
  <header class="header">
    <div class="map" role="img" aria-label="Small map of the United Kingdom"></div>
    <div class="brand">LODGING MEADOW</div>
    <div class="tagline">OVER 30,000 PLACES TO STAY IN THE UK</div>
  </header>
  <nav class="nav"><a>HOTELS</a><a>CAMPSITES</a><a>MORE FUN</a><a>CONTACT</a></nav>
  <div class="strip">
    <div class="p1" role="img" aria-label="Palace facade with gardens"></div>
    <div class="p2" role="img" aria-label="Clock tower by the river"></div>
    <div class="p3" role="img" aria-label="Lit hotel entrance at night"></div>
    <div class="p4" role="img" aria-label="Tower bridge over the river"></div>
  </div>
  <div class="body">
    <aside class="side">
      <h4>TRAVEL GUIDE</h4>
      <div class="rule"></div>
      <h4>SEARCH</h4>
      <div>Search this site:</div>
      <input type="text" aria-label="Search this site">
      <span class="btn">Search</span>
      <div class="hotels">
        <h5>Search Hotels</h5>
        <div class="sel">Select region</div>
        <div class="sel">Tue 20 Jun 2024</div>
        <div class="sel">1 night</div>
        <div class="sel">1 person</div>
        <div class="sel">Any type</div>
        <div style="text-align:right"><span class="btn">Search</span></div>
      </div>
      <h4>LINKS</h4>
      <ul><li>Seasonal offers</li><li>Regional guides</li><li>Late rooms</li><li>Holiday cottages</li></ul>
      <h4>SPONSORED ADS</h4>
      <div>Space reserved for partner adverts here</div>
      <div class="ads">Useful Links</div>
      <ul><li>Travel tips</li></ul>
    </aside>
    <main class="main">
      <div class="sec">USEFUL INFO</div>
      <div class="bar"></div>
      <div class="title">What Are the Best Things About Britain</div>
      <div class="meta">Posted by Verano Loft in Articles | 0 comments</div>
      <a class="more">Read More</a>
      <div class="sec" style="margin-top:14px">Hotels</div>
      <div class="bar">Find a place to stay</div>
      <div class="welcome">
        <div>
          <h3>Welcome</h3>
          <p>Browse a wide choice of hotels, guesthouses and cottages across every part of Britain. Search by region, compare prices and book directly with owners who know their area well. Every listing is checked so you can plan the perfect trip.</p>
          <a class="more">Read More</a>
        </div>
        <div class="hotelphoto" role="img" aria-label="Example hotel frontage at dusk"></div>
      </div>
      <div class="cards">
        <div class="card">
          <div class="row"><div class="img c1" role="img" aria-label="Palace with flower beds"></div><div class="side-t">Palace<br>view</div></div>
          <h6>Interested in purchasing a high quality print or poster of this image?</h6>
          <p>Order a framed print in several sizes, delivered to your door within a few working days.</p>
        </div>
        <div class="card">
          <div class="row"><div class="img c2" role="img" aria-label="Clock tower against blue sky"></div><div class="side-t">Interested<br>in</div></div>
          <h6>purchasing a high quality print or poster of this image?</h6>
          <p>Choose paper or canvas finish and we will print and ship it quickly across the UK.</p>
        </div>
      </div>
    </main>
  </div>
  <footer class="footer">
    <span class="dot"></span>
    Copyright © 2024 lodgingmeadow.co.uk. All Rights Reserved.<br>Terms · Privacy · Contact
  </footer>
</div>
<div class="powered">Powered by Lodging Meadow</div>
</body>
</html>
```